Flyer Design - You Need a Mobile Website

We need an A4 size flyer design for print to be used as part of a Direct Mail package.

The target audience is small business owners, such as Vets, Dentists, Plumbers and others who would benefit from owning a Mobile Website.

"You're not fully open for business until you have a mobile website." is the theme.

Our product is a mobile-phone/smartphone optimized version of the client's normal desktop website, automatically updated as the main web-site is changed.

The desired course of action is for the reader to go to the website and order a FREE preview.

IMPORTANT NOTE: 4-9-2013 we have revieds some of the wording see File4 "Get your Mobile Website Built Free of charge"

Target Market(s)

Small Business Owners, businesses that provide emergency/urgent services. (eg Vets, Dentist, Plumber etc)

Industry/Entity Type

Small Business

Requirements
Must have
• Design must comply with the printers specification for A4 flyers, details are here: http://www.printvarolo.com.au/Templates/A4Templates/tabid/142/default.aspx
(Photoshop version is attached)

Proposed Text is attached (see attachment 1 "You're not fully open for business until you have a mobile website")
Nice to have
• Further background explanation is attached. (see attachment 2 "Brindlecove Mobile Websites Flyer-Explanation")

```html
<!DOCTYPE html>
<html lang="en">
<head>
<meta charset="utf-8">
<title>Brindlecove Mobile Websites Flyer</title>
<link rel="stylesheet" href="https://fonts.googleapis.com/css2?family=Raleway:wght@300;400;500;600&display=swap">
<style>
  :root {
    --brand-blue: #2a8bc8;
    --light-blue: #4fa6dc;
    --ink: #3b3b3d;
    --muted: #9a9b9e;
    --dark-grey: #4a4b4d;
    --paper: #ffffff;
  }
  * { box-sizing: border-box; margin: 0; padding: 0; }
  html, body { width: 848px; height: 1200px; overflow: hidden; background: var(--paper); }
  body { font-family: "Raleway", sans-serif; color: var(--ink); }
  .flyer { position: relative; width: 848px; height: 1200px; overflow: hidden; }
  .abs { position: absolute; }

  .headline { left: 37px; top: 28px; }
  .headline span {
    display: table; background: var(--brand-blue); color: #fff;
    font-weight: 500; font-size: 52px; line-height: 50px; letter-spacing: 1px;
    padding: 2px 6px 0 4px; margin-bottom: 6px; text-transform: uppercase;
  }

  .intro { left: 37px; top: 256px; width: 390px; font-size: 19px; line-height: 24px; font-weight: 400; }
  .stats-title { left: 37px; top: 418px; width: 400px; font-size: 23px; line-height: 28px; font-weight: 500; }
  .stat { left: 37px; display: flex; align-items: center; }
  .stat-value { font-size: 46px; font-weight: 300; color: var(--light-blue); width: 96px; letter-spacing: -1px; line-height: 40px; }
  .stat-label { font-size: 16px; line-height: 18px; padding-top: 4px; }

  .why-title { left: 440px; top: 258px; font-size: 24px; font-weight: 500; }
  .chev-list { list-style: none; font-size: 16.5px; line-height: 20.6px; }
  .chev-list li { position: relative; padding-left: 18px; }
  .chev-list li::before {
    content: ""; position: absolute; left: 2px; top: 7px; width: 6px; height: 6px;
    border-top: 3px solid var(--brand-blue); border-right: 3px solid var(--brand-blue); transform: rotate(45deg);
  }
  .why-list { left: 440px; top: 302px; }
  .footnote { left: 466px; top: 466px; width: 330px; font-size: 12px; line-height: 15px; }

  .art { background: linear-gradient(160deg, #4fa6dc, #2a8bc8); border-radius: 6px; }

  .vs-band { left: 0; top: 630px; width: 848px; height: 32px; background: var(--brand-blue); color: #fff; font-size: 22px; font-weight: 500; }
  .vs-band .left { position: absolute; right: 470px; top: 2px; }
  .vs-band .right { position: absolute; left: 468px; top: 2px; }
  .vs-badge {
    left: 396px; top: 618px; width: 56px; height: 56px; border-radius: 50%;
    background: var(--dark-grey); border: 3px solid #fff; color: #fff;
    font-size: 22px; font-weight: 600; text-align: center; line-height: 50px;
  }

  .std-list { right: 450px; top: 674px; text-align: right; font-size: 16.5px; line-height: 20.6px; list-style: none; }
  .std-list li { position: relative; padding-right: 18px; }
  .std-list li::after {
    content: ""; position: absolute; right: 2px; top: 7px; width: 6px; height: 6px;
    border-bottom: 3px solid var(--brand-blue); border-left: 3px solid var(--brand-blue); transform: rotate(45deg);
  }
  .mobile-list { left: 458px; top: 674px; width: 340px; }

  .phone-label { top: 955px; font-size: 14px; color: var(--light-blue); }

  .cta-band { left: 141px; top: 1012px; width: 673px; height: 34px; background: var(--brand-blue); color: #fff; font-size: 25px; font-weight: 500; padding: 2px 0 0 8px; letter-spacing: 0.5px; }
  .free-badge { left: 36px; top: 985px; }
  .cta-text { left: 150px; top: 1058px; width: 270px; font-size: 16.5px; line-height: 19.5px; }
  .cta-text b { font-weight: 600; }
  .cta-note { left: 150px; top: 1121px; width: 270px; font-size: 15px; line-height: 18px; color: var(--muted); }
  .company { left: 476px; top: 1058px; font-size: 16.5px; line-height: 19.5px; }
  .contact { left: 476px; top: 1121px; font-size: 15px; line-height: 18px; color: var(--muted); }
  .contact .web { color: var(--ink); font-weight: 600; }
</style>
</head>
<body>
<main class="flyer">
  <h1 class="abs headline">
    <span>You're not</span>
    <span>fully open for business</span>
    <span>until you have a mobile</span>
    <span>website</span>
  </h1>

  <p class="abs intro">More than half of all Australians are using their mobile phones to access the web. That means that half of your customers are too. Now, all businesses need a Mobile Website just to keep up with their competitors.</p>

  <h2 class="abs stats-title">In 2012 Australian Smartphone users accessed the internet:</h2>
  <div class="abs stat" style="top:490px"><span class="stat-value">62%</span><span class="stat-label">looked for information<br>on products and services</span></div>
  <div class="abs stat" style="top:533px"><span class="stat-value">55%</span><span class="stat-label">looked for suppliers<br>of products or services</span></div>
  <div class="abs stat" style="top:576px"><span class="stat-value">33%</span><span class="stat-label">ordered<br>goods or services</span></div>

  <h2 class="abs why-title">Why get a Mobile Website?</h2>
  <ul class="abs chev-list why-list">
    <li>To get more website traffic*</li>
    <li>To Boost your brand</li>
    <li>To Generate new leads</li>
    <li>To Increase sales and revenue.</li>
    <li>To avoid frustrating your audience</li>
    <li>To step into the digital age</li>
    <li>To stay ahead of the competition</li>
  </ul>
  <p class="abs footnote">*Adding a mobile friendly site results in an overall traffic increase of 18% (source: Marlow Research)</p>

  <svg class="abs growth-icon" style="left:470px;top:520px" width="84" height="84" viewBox="0 0 84 84" aria-label="Growth chart icon">
    <path d="M4 2 V80 H82" fill="none" stroke="var(--brand-blue)" stroke-width="3"/>
    <path d="M12 68 L30 46 L42 56 L70 20" fill="none" stroke="var(--brand-blue)" stroke-width="3"/>
    <path d="M60 18 L72 16 L71 28" fill="none" stroke="var(--brand-blue)" stroke-width="3"/>
  </svg>
  <div class="abs art" style="left:590px;top:522px;width:88px;height:80px" role="img" aria-label="Icon of three people"></div>
  <div class="abs art" style="left:718px;top:522px;width:82px;height:80px" role="img" aria-label="Icon of a friendly character head"></div>

  <div class="abs vs-band"><span class="left">Standard Website</span><span class="right">Mobile Website</span></div>
  <div class="abs vs-badge">VS</div>

  <ul class="abs std-list">
    <li>Text is too small</li>
    <li>Must Pinch, zoom and scroll to read</li>
    <li>Links are too small for touch navigation</li>
  </ul>
  <ul class="abs chev-list mobile-list">
    <li>Finger friendly navigation easy to use</li>
    <li>Click to call button, makes it easy for customers to contact you directly</li>
    <li>Mobile maps with find us button</li>
    <li>Automatically updates when you change your regular website</li>
    <li>Works on All Smartphones</li>
  </ul>

  <div class="abs art" style="left:104px;top:745px;width:130px;height:202px" role="img" aria-label="Smartphone showing a desktop website that is not mobile friendly"></div>
  <div class="abs art" style="left:246px;top:745px;width:116px;height:202px" role="img" aria-label="Smartphone showing a mobile friendly website with large buttons"></div>
  <span class="abs phone-label" style="left:108px">Not Mobile Friendly</span>
  <span class="abs phone-label" style="left:252px">Mobile Friendly</span>

  <div class="abs art" style="left:458px;top:826px;width:302px;height:118px" role="img" aria-label="Phone, laptop and tablet showing the same responsive website"></div>

  <svg class="abs free-badge" width="92" height="158" viewBox="0 0 92 158" aria-label="Free badge">
    <path d="M28 80 V154 L40 142 L52 154 V80 Z" fill="var(--brand-blue)"/>
    <circle cx="46" cy="46" r="44" fill="var(--brand-blue)"/>
    <circle cx="46" cy="46" r="36" fill="none" stroke="#fff" stroke-width="2"/>
    <text x="46" y="54" text-anchor="middle" fill="#fff" font-family="Raleway, sans-serif" font-weight="600" font-size="22">FREE</text>
  </svg>

  <div class="abs cta-band">GET A MOBILE WEBSITE PREVIEW FOR FREE</div>
  <p class="abs cta-text">go to <b>www.brindlecove.com.au/offer</b> to order your Mobile Website Preview</p>
  <p class="abs cta-note">Within a few hours Brindlecove will build your new Mobile Website. Totally FREE to you. (Normally $199 value)</p>

  <p class="abs company">BRINDLECOVE CORPORATION Pty Ltd<br>ABN 47 512 708 264<br>Level 4, 81 Harwick Lane Melbourne</p>
  <p class="abs contact">P.O. Box 742 Eastvale Victoria 3199<br>Tel: 03 9555 0184<br>Email: hello@brindlecove.com.au<br><span class="web">www.brindlecove.com.au</span></p>
</main>
</body>
</html>
```